New Brochure Design Project *

I am in need of a brochure design/layout that 'Wows' prospective customers and provides essential information about our company.
The name of the Company is Rolly Dex Charter Fishing Service.
Located in Port Washington, Wisconsin.
We take customers fishing on Lake Michigan . We have been in business for over 30 years with a reputation for the most successful fishing charter in the area. Voted best fishing Charter for several years in a row. We fish for Chinook Salmon, Steelhead, Brown Trout, Coho Salmon and Lake Trout. Our fleet of 4 large fishing boats are well maintained and fully equipped with all fishing tackle , the latest in fishing gear and electronics, private restroom, heat and air. Fully insured. Our boats are U.S. Coast Guard Certified and licensed to accommodate 1 to 6 passengers.
Our selected Captains have over 100 years of experience fishing Lake Michigan .
Target market: Corporations that provide team building exercises,/ rewards employees for a job well done/ entertain clients, Outdoor enthusiasts, Men, women and families that enjoy fresh water fishing.
Design specifics: I would like to have 5-7 photos of our catch, ( I can provide those ) photos of the 4 boats ( I will provide ) Our Logo ( I will provide ) A page for our rates and packages, our website, contact information.
Our current brochure can be viewed on our website under the downloadable brochure tab. At www.rollydexcharters.example Our Facebook www.facebook.com/RollyDexChartersLLC page is a great way to learn more about us as well and responses from our customers plus reviews of our Company for reference. I am open to advice on this project.
Our current brochure is a colored two sided brochure with 5 panels that fold up ( almost accordion style ) with a front and back cover. I am open to new layouts and easier folding options.
Attached is our logo, and current brochure. I will send photos as needed.( I will be making price adjustments for the new brochure)
Thank you so much for your help.

```html
<!DOCTYPE html>
<html lang="en">
<head>
<meta charset="utf-8">
<title>Rolly Dex Charter Fishing Service – Brochure Spread</title>
<link rel="stylesheet" href="https://fonts.googleapis.com/css2?family=Montserrat:wght@400;500;600;700;800;900&family=Oswald:wght@300;400&display=swap">
<style>
  :root{
    --navy:#1f3f7a;
    --navy-deep:#17305f;
    --slate:#3d5f98;
    --sky:#2ea3dc;
    --sky-soft:#8fc3e6;
    --paper:#ffffff;
    --mist:#e5e8ed;
    --ink:#505663;
    --ink-soft:#6b717d;
  }
  *{box-sizing:border-box;margin:0;padding:0}
  html,body{width:1200px;height:759px;overflow:hidden;background:#f3f4f6}
  body{font-family:"Montserrat",Arial,sans-serif;color:var(--ink)}
  .spread{position:relative;width:1200px;height:759px;background:var(--paper)}
  .page{position:absolute;top:0;width:600px;height:759px;overflow:hidden}
  .page--left{left:0;background:var(--mist)}
  .page--right{left:600px;background:var(--paper)}
  .page svg.art{position:absolute;inset:0}
  .footer-band{position:absolute;left:0;right:0;bottom:0;height:38px;background:var(--navy)}

  /* left page text */
  .intro{position:absolute;left:36px;top:24px;width:290px}
  .intro__kicker{font-family:"Oswald",sans-serif;font-weight:300;font-size:34px;color:var(--sky);line-height:1}
  .intro__title{font-weight:800;font-size:19px;color:var(--navy);letter-spacing:.5px;margin-top:2px;padding-bottom:6px;border-bottom:2px solid var(--navy);display:inline-block}
  .intro__body{font-size:11px;line-height:1.45;color:var(--ink-soft);margin-top:8px;width:270px}
  .intro__sub{margin-top:10px;font-weight:700;font-size:14px;color:var(--navy)}
  .intro__sub span{font-weight:400;color:var(--sky);text-decoration:underline}
  .captains{list-style:none;margin-top:6px;font-size:11px;line-height:1.4;color:var(--ink-soft);width:280px}
  .captains li{position:relative;padding-left:14px;margin-bottom:5px}
  .captains li::before{content:"";position:absolute;left:0;top:4px;border-left:6px solid var(--ink);border-top:4px solid transparent;border-bottom:4px solid transparent}
  .captains b{color:var(--ink);font-weight:700}

  .furnish{position:absolute;left:36px;top:410px;width:300px}
  .furnish__title{font-weight:800;font-size:15px;color:var(--navy);letter-spacing:.4px}
  .furnish__title span{font-weight:400;color:var(--sky)}
  .furnish__list{list-style:none;margin-top:8px}
  .furnish__list li{display:flex;align-items:center;gap:10px;font-size:11.5px;font-weight:500;color:var(--ink-soft);height:32px}
  .furnish__list svg{flex:0 0 26px}
  .claim{position:absolute;left:36px;top:606px;font-weight:700;font-size:17px;line-height:1.05;color:var(--sky-soft);letter-spacing:.5px}
  .claim b{display:block;color:var(--navy);font-weight:800}

  .boat-label{position:absolute;font-weight:700;color:#fff;font-size:15px;letter-spacing:1px;white-space:nowrap}
  .boat-label--dark{color:var(--navy)}

  /* right page */
  .season-title{position:absolute;left:36px;top:66px;font-weight:900;line-height:1;font-size:36px}
  .season-title .t1,.season-title .t3{color:var(--sky);font-style:italic}
  .season-title .t2{color:#fff;font-size:40px}
  .icon-tile{position:absolute;width:58px;height:58px;transform:rotate(45deg);display:flex;align-items:center;justify-content:center;border:3px solid #fff}
  .icon-tile svg{transform:rotate(-45deg)}
  .icon-tile--sky{background:var(--sky)}
  .icon-tile--navy{background:var(--navy)}

  .calendar{position:absolute;top:368px;width:262px}
  .calendar--a{left:28px}
  .calendar--b{left:310px;top:376px}
  .slot{margin-bottom:12px}
  .slot__date{display:flex;align-items:baseline;gap:6px;font-weight:800;font-size:11.5px;color:var(--navy);letter-spacing:.3px;margin-bottom:4px}
  .slot__date svg{align-self:center}
  .slot__date .num{font-style:italic;font-size:16px;color:var(--sky)}
  .slot__date sup{font-size:8px;color:var(--sky)}
  .slot p{font-size:10.6px;line-height:1.42;color:var(--ink-soft)}
  .slot p b{color:var(--navy);font-weight:800}
  .tagline{position:absolute;left:310px;top:684px;font-weight:800;font-size:12.5px;color:var(--navy);letter-spacing:.4px}
</style>
</head>
<body>
<main class="spread">

  <!-- LEFT PAGE -->
  <section class="page page--left">
    <svg class="art" width="600" height="759" viewBox="0 0 600 759">
      <defs>
        <linearGradient id="seaA" x1="0" y1="0" x2="0" y2="1">
          <stop offset="0" stop-color="#cfdceb"/><stop offset=".55" stop-color="#a9c3dc"/><stop offset="1" stop-color="#3f7fae"/>
        </linearGradient>
        <linearGradient id="seaB" x1="0" y1="0" x2="0" y2="1">
          <stop offset="0" stop-color="#d9e4ef"/><stop offset=".5" stop-color="#8db3d3"/><stop offset="1" stop-color="#2f6fa3"/>
        </linearGradient>
        <linearGradient id="seaC" x1="0" y1="0" x2="0" y2="1">
          <stop offset="0" stop-color="#7f9fbd"/><stop offset=".5" stop-color="#3f6f98"/><stop offset="1" stop-color="#1f4e78"/>
        </linearGradient>
      </defs>
      <rect x="36" y="284" width="70" height="96" fill="var(--slate)"/>
      <polygon points="330,0 600,0 600,236 470,390" fill="url(#seaA)" stroke="#fff" stroke-width="6" role="img" aria-label="Photo of the charter boat Rolly Dex on Lake Michigan"/>
      <polygon points="80,290 400,300 470,390 80,372" fill="url(#seaB)" stroke="#fff" stroke-width="6" role="img" aria-label="Photo of the charter boat Rolly Dex VI cruising"/>
      <polygon points="600,240 470,390 600,610" fill="url(#seaC)" stroke="#fff" stroke-width="6" role="img" aria-label="Photo of the stern of Rolly Dex II in Port Washington harbor"/>
      <polygon points="470,390 600,614 600,721 236,721" fill="url(#seaB)" stroke="#fff" stroke-width="6" role="img" aria-label="Photo of the charter boat Rolly Dex III underway"/>
    </svg>

    <div class="intro">
      <div class="intro__kicker">Over 30 years</div>
      <div class="intro__title">IN BUSINESS!</div>
      <p class="intro__body">We take pride in our boats and our business. Rolly Dex's selected Captains are the key to a successful fishing trip.</p>
      <div class="intro__sub"><span>These</span> Include:</div>
      <ul class="captains">
        <li><b>CAPTAIN TOM RELLER</b>, 37 years as a licensed Captain on Lake Michigan.</li>
        <li><b>CAPTAIN DAN MARSH</b>, 14 years as a licensed Captain with over 25 years fishing experience on Lake Michigan.</li>
      </ul>
    </div>

    <span class="boat-label" style="left:430px;top:190px;transform:rotate(20deg)">ROLLY DEX</span>
    <span class="boat-label boat-label--dark" style="left:120px;top:306px;transform:rotate(8deg)">ROLLY DEX VI</span>
    <span class="boat-label" style="left:505px;top:430px;transform:rotate(60deg);font-size:12px">ROLLY DEX II</span>
    <span class="boat-label" style="left:360px;top:640px;transform:rotate(18deg)">ROLLY DEX III</span>

    <div class="furnish">
      <div class="furnish__title"><span>BOAT</span> FURNISHINGS:</div>
      <ul class="furnish__list">
        <li><svg width="26" height="26" viewBox="0 0 26 26"><circle cx="13" cy="13" r="11.5" fill="none" stroke="var(--navy)" stroke-width="1.5"/><path d="M7 19 L19 7 M15 9 q3 5 -1 8" fill="none" stroke="var(--navy)" stroke-width="1.5"/></svg>All Fishing Tackle</li>
        <li><svg width="26" height="26" viewBox="0 0 26 26"><circle cx="13" cy="13" r="11.5" fill="none" stroke="var(--navy)" stroke-width="1.5"/><rect x="8" y="9" width="10" height="7" rx="1" fill="none" stroke="var(--navy)" stroke-width="1.5"/><path d="M11 19h4" stroke="var(--navy)" stroke-width="1.5"/></svg>The Latest in Fishing Gear and Electronics</li>
        <li><svg width="26" height="26" viewBox="0 0 26 26"><circle cx="13" cy="13" r="11.5" fill="none" stroke="var(--navy)" stroke-width="1.5"/><path d="M8 18V11l5-4 5 4v7z" fill="none" stroke="var(--navy)" stroke-width="1.5"/></svg>Private Restroom, Heat &amp; Air</li>
        <li><svg width="26" height="26" viewBox="0 0 26 26"><circle cx="13" cy="13" r="11.5" fill="none" stroke="var(--navy)" stroke-width="1.5"/><path d="M13 6l6 2v5c0 4-3 6-6 7-3-1-6-3-6-7V8z" fill="none" stroke="var(--navy)" stroke-width="1.5"/></svg>Fully Insured</li>
      </ul>
    </div>
    <div class="claim">BEST BOATS,<br>MOST TRIPS,<br>MOST FISH,<b>PERIOD!</b></div>

    <div class="footer-band"></div>
  </section>

  <!-- RIGHT PAGE -->
  <section class="page page--right">
    <svg class="art" width="600" height="759" viewBox="0 0 600 759">
      <defs>
        <linearGradient id="sky" x1="0" y1="0" x2="0" y2="1">
          <stop offset="0" stop-color="#4f86c2"/><stop offset=".6" stop-color="#9cc3e4"/><stop offset="1" stop-color="#5d8fbf"/>
        </linearGradient>
        <linearGradient id="deck" x1="0" y1="0" x2="1" y2="0">
          <stop offset="0" stop-color="#9aa6b3"/><stop offset=".5" stop-color="#b86b62"/><stop offset="1" stop-color="#8a97a6"/>
        </linearGradient>
      </defs>
      <polygon points="0,0 250,0 330,215 0,380" fill="var(--slate)"/>
      <polygon points="262,0 600,0 600,300 350,300" fill="url(#sky)" stroke="#fff" stroke-width="8" role="img" aria-label="Photo of anglers reeling in a fish under a blue sky"/>
      <polygon points="80,300 270,262 330,340 60,346" fill="url(#deck)" stroke="#fff" stroke-width="6" role="img" aria-label="Photo of a happy group with their catch on deck"/>
    </svg>

    <h1 class="season-title"><span class="t1">Fishing</span><br><span class="t2">SEASON</span><br><span class="t3">Calendar</span></h1>

    <div class="icon-tile icon-tile--sky" style="left:262px;top:168px">
      <svg width="30" height="30" viewBox="0 0 30 30"><rect x="4" y="6" width="22" height="19" rx="2" fill="#fff"/><g fill="var(--sky)"><rect x="7" y="12" width="4" height="3"/><rect x="13" y="12" width="4" height="3"/><rect x="19" y="12" width="4" height="3"/><rect x="7" y="18" width="4" height="3"/><rect x="13" y="18" width="4" height="3"/><rect x="19" y="18" width="4" height="3"/></g></svg>
    </div>
    <div class="icon-tile icon-tile--navy" style="left:306px;top:212px">
      <svg width="30" height="30" viewBox="0 0 30 30"><circle cx="15" cy="15" r="10" fill="none" stroke="#fff" stroke-width="2.2"/><path d="M15 9v6l4 3" fill="none" stroke="#fff" stroke-width="2.2"/></svg>
    </div>
    <div class="icon-tile icon-tile--sky" style="left:350px;top:256px">
      <svg width="32" height="32" viewBox="0 0 32 32"><path d="M5 16c5-7 14-7 19 0-5 7-14 7-19 0zM24 16l5-5v10z" fill="#fff"/><circle cx="10" cy="15" r="1.4" fill="var(--sky)"/></svg>
    </div>

    <div class="calendar calendar--a">
      <div class="slot">
        <div class="slot__date"><svg width="12" height="10" viewBox="0 0 12 10"><rect width="12" height="10" rx="1" fill="var(--navy)"/></svg>APRIL <span class="num">15<sup>TH</sup></span> THRU MAY <span class="num">30<sup>TH</sup></span></div>
        <p>Kick start the season targeting Brown Trout, Lake Trout, and Steelhead. One of the best opportunities for Trophy size Brown and Lake Trout. <b>BOOK EARLY.</b> These dates will fill up fast.</p>
      </div>
      <div class="slot">
        <div class="slot__date"><svg width="12" height="10" viewBox="0 0 12 10"><rect width="12" height="10" rx="1" fill="var(--navy)"/></svg>JUNE <span class="num">1<sup>ST</sup></span> THRU JUNE <span class="num">30<sup>TH</sup></span></div>
        <p>June is the month for abundant catches of Large Steelhead and Coho Salmon. We leave from picturesque Port Washington Harbor for hours of spectacular fun and productive fishing.</p>
      </div>
      <div class="slot">
        <div class="slot__date"><svg width="12" height="10" viewBox="0 0 12 10"><rect width="12" height="10" rx="1" fill="var(--navy)"/></svg>JULY <span class="num">1<sup>ST</sup></span> THRU JULY <span class="num">31<sup>ST</sup></span></div>
        <p>For the best King Salmon fishing on Lake Michigan, the place to be is with "Rolly Dex" as we leave from the Port Washington Harbor. The "Kings" range from the 20 to 30 pound class. Intermixed with the "Kings", prepare to experience some terrific Large Steelhead and Coho Salmon action.</p>
      </div>
    </div>

    <div class="calendar calendar--b">
      <div class="slot">
        <div class="slot__date"><svg width="12" height="10" viewBox="0 0 12 10"><rect width="12" height="10" rx="1" fill="var(--navy)"/></svg>AUGUST <span class="num">1<sup>ST</sup></span> THRU AUGUST <span class="num">31<sup>ST</sup></span></div>
        <p>What a month! Catches of 15 to 20 fish per trip are common from the Port Washington Harbor. Our main target during this period is the fantastic King Salmon. These beauties can range up to 30 pounds plus.</p>
      </div>
      <div class="slot">
        <div class="slot__date"><svg width="12" height="10" viewBox="0 0 12 10"><rect width="12" height="10" rx="1" fill="var(--navy)"/></svg>SEPTEMBER <span class="num">1<sup>ST</sup></span> THRU OCTOBER <span class="num">15<sup>TH</sup></span></div>
        <p>With the arrival of Fall the King Salmon have reached the peak of their weight class and moving to the shallower water of the harbor and shoreline to spawn. We go out to harvest the large "Kings" in the early to late morning. Later we move off shore for a variety of two and three year old Salmon.</p>
      </div>
      <div class="slot">
        <p>Brown Trout are also on our radar, reaching weights of up to 30 pounds.</p>
      </div>
    </div>
    <div class="tagline">WE'LL GO THE EXTRA MILE...OR 20!</div>

    <div class="footer-band"></div>
  </section>

</main>
</body>
</html>
```